Ferro Lanes - explore habits of productive people

Ferro Lanes is a social place around habits and productivity

The full brief below:

https://files.quorvanta.com/sheet/d/7Kp-RwTZMX2uqEebH-Y-cNdt4TgsWmFkyQoPJhwbrzVe/view?mode=viewer

Colors

Designer to choose colors to be used in the design.

Requirements
Must have
• - a feed page to display habits
• - a habit page to add a habit
• / clean, no cluttered design, lots of white space
• / inspired by material design or other design system
Nice to have
• - user page

```html
<!DOCTYPE html>
<html lang="en">
<head>
<meta charset="utf-8">
<title>Ferro Lanes – Habit Feeds</title>
<link rel="stylesheet" href="https://fonts.googleapis.com/css2?family=Montserrat:wght@500;600;700;800&family=Open+Sans:wght@400;600&display=swap">
<style>
  :root {
    --bg: #f2f3f5;
    --surface: #ffffff;
    --ink: #2b2b33;
    --ink-soft: #3a3a42;
    --muted: #8d8e96;
    --faint: #c5c6cc;
    --line: #dcdde2;
    --accent: #5e6bb5;
    --accent-soft: #8b95d8;
    --good: #5cc548;
    --bad: #e0186b;
    --avatar-a: #b39a86;
    --avatar-b: #3a3a3a;
    --avatar-c: #9a7a66;
    --avatar-d: #4a4442;
  }
  * { box-sizing: border-box; margin: 0; padding: 0; }
  html, body { width: 1161px; height: 1200px; overflow: hidden; background: var(--bg); }
  body { font-family: "Open Sans", sans-serif; color: var(--ink); }
  .page { position: relative; width: 1200px; height: 1240px; transform: scale(0.9675); transform-origin: top left; }

  .topbar { position: absolute; left: 0; top: 0; width: 1200px; height: 76px; background: var(--surface); box-shadow: 0 4px 24px rgba(40,44,70,0.05); }
  .brand { position: absolute; left: 30px; top: 22px; font-family: "Montserrat", sans-serif; font-weight: 800; font-size: 22px; letter-spacing: -0.5px; color: var(--ink); }
  .account { position: absolute; left: 1108px; top: 20px; display: flex; align-items: center; gap: 10px; }
  .avatar { display: block; border-radius: 50%; flex: none; }
  .account .avatar { width: 36px; height: 36px; background: var(--avatar-d); }

  .feed { position: absolute; left: 240px; top: 135px; width: 720px; }
  .feed-title { font-family: "Montserrat", sans-serif; font-weight: 800; font-size: 35px; color: var(--ink); letter-spacing: -0.3px; }
  .view-links { margin-top: 8px; display: flex; align-items: center; font-family: "Montserrat", sans-serif; font-weight: 500; font-size: 13px; color: var(--accent); }
  .view-links .sep { width: 1px; height: 16px; background: var(--line); margin: 0 14px; }
  .add-btn { position: absolute; left: 659px; top: 10px; width: 52px; height: 52px; border-radius: 50%; background: var(--accent-soft); box-shadow: 0 6px 16px rgba(94,107,181,0.25); display: flex; align-items: center; justify-content: center; }

  .tabs { position: relative; margin-top: 40px; height: 68px; border-bottom: 1px solid var(--line); font-family: "Montserrat", sans-serif; font-weight: 500; font-size: 14px; color: var(--accent); }
  .tab { position: absolute; top: 21px; transform: translateX(-50%); white-space: nowrap; }
  .tab.active { font-weight: 700; }
  .tab-indicator { position: absolute; left: 9px; bottom: -1px; width: 108px; height: 3px; background: var(--accent-soft); }
  .tab-more { position: absolute; left: 680px; top: 31px; display: flex; gap: 3px; }
  .tab-more i { width: 4px; height: 4px; border-radius: 50%; background: var(--accent-soft); }

  .habit-list { margin-top: 25px; display: flex; flex-direction: column; gap: 2px; }
  .habit { background: var(--surface); border-radius: 4px; box-shadow: 0 2px 10px rgba(40,44,70,0.04); }
  .habit.open { margin-bottom: 10px; padding-bottom: 52px; }
  .habit-head { height: 70px; display: flex; align-items: center; padding: 0 20px 0 19px; }
  .toggle { width: 28px; height: 28px; border-radius: 50%; border: 1.5px solid #d9dadf; display: flex; align-items: center; justify-content: center; flex: none; }
  .habit-head .avatar { width: 36px; height: 36px; margin-left: 19px; }
  .habit-name { margin-left: 10px; font-size: 18px; color: var(--ink-soft); white-space: nowrap; overflow: hidden; text-overflow: ellipsis; max-width: 390px; }
  .tag { margin-left: 11px; height: 26px; padding: 0 12px; border-radius: 13px; border: 2px solid var(--good); color: var(--good); font-family: "Montserrat", sans-serif; font-weight: 600; font-size: 13px; display: flex; align-items: center; flex: none; }
  .tag.bad { border-color: var(--bad); color: var(--bad); }
  .like { margin-left: auto; width: 110px; height: 34px; border-radius: 17px; border: 1px solid var(--accent-soft); color: var(--accent-soft); font-family: "Montserrat", sans-serif; font-weight: 500; font-size: 12px; display: flex; align-items: center; justify-content: center; gap: 7px; flex: none; }
  .like.liked { background: var(--accent); border-color: var(--accent); color: #fff; font-weight: 600; }

  .loop-grid { display: grid; grid-template-columns: 355px 1fr; row-gap: 34px; padding: 24px 0 0 60px; }
  .loop { height: 50px; }
  .loop:nth-child(odd) { border-right: 1px solid var(--line); }
  .loop:nth-child(even) { padding-left: 33px; }
  .loop-label { display: flex; align-items: center; gap: 8px; font-size: 12px; color: var(--muted); text-transform: uppercase; }
  .loop-label svg { flex: none; }
  .loop-value { margin: 14px 0 0 23px; font-size: 14px; color: var(--ink-soft); }

  .loading { position: absolute; left: 550px; top: 939px; display: flex; align-items: center; gap: 10px; font-size: 12px; color: var(--accent-soft); }
  .footer { position: absolute; left: 240px; top: 1120px; width: 720px; border-top: 1px solid var(--line); text-align: center; }
  .footer-brand { margin-top: 28px; font-family: "Montserrat", sans-serif; font-weight: 800; font-size: 22px; letter-spacing: -0.5px; color: var(--faint); }
  .copyright { margin-top: 6px; font-size: 12px; color: var(--muted); }
</style>
</head>
<body>
<div class="page">
  <header class="topbar">
    <div class="brand">ferrolanes</div>
    <div class="account">
      <span class="avatar" role="img" aria-label="Profile photo of the signed-in member"></span>
      <svg width="18" height="10" viewBox="0 0 18 10"><path d="M2 2l7 6 7-6" fill="none" stroke="#d0d1d6" stroke-width="1.5"/></svg>
    </div>
  </header>

  <main class="feed">
    <h1 class="feed-title">Habit Feeds</h1>
    <div class="view-links"><span>Expand All</span><span class="sep"></span><span>Collapse All</span></div>
    <div class="add-btn"><svg width="20" height="20" viewBox="0 0 20 20"><path d="M10 2v16M2 10h16" stroke="#fff" stroke-width="2" stroke-linecap="round"/></svg></div>

    <nav class="tabs">
      <span class="tab active" style="left:63px">All</span>
      <span class="tab" style="left:176px">Good</span>
      <span class="tab" style="left:276px">Bad</span>
      <span class="tab" style="left:377px">Popular</span>
      <span class="tab" style="left:503px">Other Category</span>
      <span class="tab-more"><i></i><i></i><i></i></span>
      <span class="tab-indicator"></span>
    </nav>

    <section class="habit-list">
      <article class="habit open">
        <div class="habit-head">
          <span class="toggle"><svg width="12" height="8" viewBox="0 0 12 8"><path d="M1 1.5l5 5 5-5" fill="none" stroke="#c9cad0" stroke-width="1.5"/></svg></span>
          <span class="avatar" role="img" aria-label="Portrait of the habit author" style="background:var(--avatar-a)"></span>
          <span class="habit-name">An NRQ Article a day</span>
          <span class="tag">Good</span>
          <span class="like liked"><svg width="14" height="13" viewBox="0 0 14 13"><path d="M0 5h3v8H0zM4 5l3-5c1.2 0 1.8.8 1.5 2L8 4.5h4.5c1 0 1.6.8 1.4 1.7l-1.2 5.5c-.2.8-.8 1.3-1.6 1.3H4z" fill="#fff"/></svg>Liked (21)</span>
        </div>
        <div class="loop-grid">
          <div class="loop">
            <div class="loop-label"><svg width="13" height="13" viewBox="0 0 13 13"><circle cx="6.5" cy="6.5" r="6" fill="#4aa3f0"/><path d="M5 4l4 2.5L5 9z" fill="#fff"/></svg>Cue</div>
            <div class="loop-value">Morning Coffee Time</div>
          </div>
          <div class="loop">
            <div class="loop-label"><svg width="15" height="13" viewBox="0 0 15 13"><path d="M7.5 12.5S.5 8 .5 4A3.3 3.3 0 0 1 7.5 2.6 3.3 3.3 0 0 1 14.5 4c0 4-7 8.5-7 8.5z" fill="#f26a6a"/></svg>Cravings</div>
            <div class="loop-value">Learning something new</div>
          </div>
          <div class="loop">
            <div class="loop-label"><svg width="14" height="14" viewBox="0 0 14 14"><circle cx="9" cy="2" r="1.6" fill="#5cc548"/><path d="M3 5l3-1.5 3 2-1.5 3 2 2.5M7.5 8.5L5 13M6 3.5l-2.5 5H1M9 5.5l3 1" fill="none" stroke="#5cc548" stroke-width="1.4" stroke-linecap="round"/></svg>Response</div>
            <div class="loop-value">Read an article on NRQ Website</div>
          </div>
          <div class="loop">
            <div class="loop-label"><svg width="17" height="12" viewBox="0 0 17 12"><path d="M1 2l4 4 3.5-5L12 6l4-4-1.5 8h-12z" fill="#7d88cc"/><rect x="2.5" y="10.5" width="12" height="1.5" fill="#7d88cc"/></svg>Reward</div>
            <div class="loop-value">Feeling smarter</div>
          </div>
        </div>
      </article>

      <article class="habit">
        <div class="habit-head">
          <span class="toggle"><svg width="8" height="12" viewBox="0 0 8 12"><path d="M1.5 1l5 5-5 5" fill="none" stroke="#c9cad0" stroke-width="1.5"/></svg></span>
          <span class="avatar" role="img" aria-label="Portrait of the habit author" style="background:var(--avatar-b)"></span>
          <span class="habit-name">Daily Pixel</span>
          <span class="tag">Good</span>
          <span class="like liked"><svg width="14" height="13" viewBox="0 0 14 13"><path d="M0 5h3v8H0zM4 5l3-5c1.2 0 1.8.8 1.5 2L8 4.5h4.5c1 0 1.6.8 1.4 1.7l-1.2 5.5c-.2.8-.8 1.3-1.6 1.3H4z" fill="#fff"/></svg>Liked (21)</span>
        </div>
      </article>

      <article class="habit">
        <div class="habit-head">
          <span class="toggle"><svg width="8" height="12" viewBox="0 0 8 12"><path d="M1.5 1l5 5-5 5" fill="none" stroke="#c9cad0" stroke-width="1.5"/></svg></span>
          <span class="avatar" role="img" aria-label="Portrait of the habit author" style="background:var(--avatar-c)"></span>
          <span class="habit-name">Read before sleep</span>
          <span class="tag">Good</span>
          <span class="like"><svg width="14" height="13" viewBox="0 0 14 13"><path d="M0 5h3v8H0zM4 5l3-5c1.2 0 1.8.8 1.5 2L8 4.5h4.5c1 0 1.6.8 1.4 1.7l-1.2 5.5c-.2.8-.8 1.3-1.6 1.3H4z" fill="currentColor"/></svg>Like (18)</span>
        </div>
      </article>

      <article class="habit">
        <div class="habit-head">
          <span class="toggle"><svg width="8" height="12" viewBox="0 0 8 12"><path d="M1.5 1l5 5-5 5" fill="none" stroke="#c9cad0" stroke-width="1.5"/></svg></span>
          <span class="avatar" role="img" aria-label="Portrait of the habit author" style="background:var(--avatar-c)"></span>
          <span class="habit-name">Learning Machine Learning Concept on Lumora</span>
          <span class="tag">Good</span>
          <span class="like"><svg width="14" height="13" viewBox="0 0 14 13"><path d="M0 5h3v8H0zM4 5l3-5c1.2 0 1.8.8 1.5 2L8 4.5h4.5c1 0 1.6.8 1.4 1.7l-1.2 5.5c-.2.8-.8 1.3-1.6 1.3H4z" fill="currentColor"/></svg>Like (18)</span>
        </div>
      </article>

      <article class="habit">
        <div class="habit-head">
          <span class="toggle"><svg width="8" height="12" viewBox="0 0 8 12"><path d="M1.5 1l5 5-5 5" fill="none" stroke="#c9cad0" stroke-width="1.5"/></svg></span>
          <span class="avatar" role="img" aria-label="Portrait of the habit author" style="background:var(--avatar-d)"></span>
          <span class="habit-name">Sleep after eat</span>
          <span class="tag bad">Bad</span>
          <span class="like"><svg width="14" height="13" viewBox="0 0 14 13"><path d="M0 5h3v8H0zM4 5l3-5c1.2 0 1.8.8 1.5 2L8 4.5h4.5c1 0 1.6.8 1.4 1.7l-1.2 5.5c-.2.8-.8 1.3-1.6 1.3H4z" fill="currentColor"/></svg>Like (18)</span>
        </div>
      </article>
    </section>
  </main>

  <div class="loading">
    <svg width="18" height="18" viewBox="0 0 18 18" fill="#8b95d8"><circle cx="9" cy="2" r="2"/><circle cx="14" cy="4" r="1.8"/><circle cx="16" cy="9" r="1.6"/><circle cx="14" cy="14" r="1.4"/><circle cx="9" cy="16" r="1.3"/><circle cx="4" cy="14" r="1.2"/><circle cx="2" cy="9" r="1.1"/><circle cx="4" cy="4" r="1"/></svg>
    <span>Looping in ...</span>
  </div>

  <footer class="footer">
    <div class="footer-brand">ferrolanes</div>
    <div class="copyright">Copyright 2019. All rights reserved.</div>
  </footer>
</div>
</body>
</html>
```